Tide & Stone Subtitle Walk the Road of Still Waters

This is a spiritual book. It opens with a question for the readers -- Are you happy? Then proceeds to discuss the meaning of happiness, why the majority isn't and ways to achieve it. The work offers hope, and actual answers. In that regard the cover needs to relate those things.

I'm happy to contribute by answering further questions and making suggestions, however, am open to the designer letting their Spirit soar and see where it leads them.

Ask yourself the question; Am I happy, imagine finding Your happiness then designing the cover that comes from that space. Just a thought.

```html
<!DOCTYPE html>
<html lang="en">
<head>
<meta charset="utf-8">
<title>Are You Happy? – Tide &amp; Stone</title>
<link rel="stylesheet" href="https://fonts.googleapis.com/css2?family=Cinzel:wght@400;500&display=swap">
<style>
  :root {
    --page-bg: #ffffff;
    --leaf-deep: #1f3a12;
    --leaf-mid: #4f7a23;
    --leaf-bright: #9cc23c;
    --sun-glow: #fbfbe0;
    --water-dark: #2c4a16;
    --title-ink: #ffffff;
    --title-shadow: rgba(20, 40, 10, 0.5);
  }

  * { margin: 0; padding: 0; box-sizing: border-box; }

  html, body {
    width: 1200px;
    height: 900px;
    overflow: hidden;
    background: var(--page-bg);
  }

  .canvas {
    position: relative;
    width: 1200px;
    height: 900px;
    background: var(--page-bg);
  }

  .book-cover {
    position: absolute;
    left: 330px;
    top: 45px;
    width: 540px;
    height: 810px;
    overflow: hidden;
    box-shadow: 0 6px 24px rgba(0, 0, 0, 0.18);
  }

  .cover-photo {
    position: absolute;
    inset: 0;
    background:
      radial-gradient(circle at 84% 9%, var(--sun-glow) 0%, rgba(240, 245, 170, 0.85) 10%, rgba(180, 210, 80, 0.35) 28%, rgba(0, 0, 0, 0) 45%),
      radial-gradient(ellipse 70% 16% at 45% 44%, rgba(170, 205, 110, 0.55) 0%, rgba(0, 0, 0, 0) 70%),
      radial-gradient(ellipse 80% 22% at 50% 78%, rgba(190, 220, 120, 0.45) 0%, rgba(0, 0, 0, 0) 70%),
      linear-gradient(180deg, var(--leaf-deep) 0%, var(--leaf-mid) 28%, #3b5f1a 50%, var(--water-dark) 60%, var(--leaf-mid) 76%, var(--leaf-bright) 90%, #cfdca0 100%);
  }

  .cover-title {
    position: absolute;
    left: 0;
    right: 0;
    top: 72px;
    text-align: center;
    font-family: "Cinzel", "Times New Roman", serif;
    font-weight: 400;
    text-transform: uppercase;
    color: var(--title-ink);
    font-size: 100px;
    line-height: 1.18;
    letter-spacing: 0;
    text-shadow: 0 2px 8px var(--title-shadow);
  }

  .cover-title .title-line { display: block; }

  .cover-subtitle {
    position: absolute;
    left: 0;
    right: 0;
    top: 470px;
    text-align: center;
    font-family: "Cinzel", "Times New Roman", serif;
    font-weight: 400;
    font-size: 22px;
    letter-spacing: 1px;
    color: var(--title-ink);
    text-shadow: 0 1px 4px var(--title-shadow);
  }

  .cover-author {
    position: absolute;
    left: 0;
    right: 0;
    bottom: 70px;
    text-align: center;
    font-family: "Cinzel", "Times New Roman", serif;
    font-weight: 400;
    font-size: 26px;
    letter-spacing: 2px;
    text-transform: uppercase;
    color: var(--title-ink);
    text-shadow: 0 1px 4px var(--title-shadow);
  }
</style>
</head>
<body>
  <main class="canvas">
    <section class="book-cover">
      <div class="cover-photo" role="img" aria-label="Close-up of a dew-covered blade of green grass arching over rippling water, with bright sunlight bursting from the upper right"></div>
      <h1 class="cover-title">
        <span class="title-line">Are</span>
        <span class="title-line">you</span>
        <span class="title-line">Happy ?</span>
      </h1>
      <p class="cover-subtitle">Walk the Road of Still Waters</p>
      <p class="cover-author">Tide &amp; Stone</p>
    </section>
  </main>
</body>
</html>
```